Web Design for an Online Dating Web Site

We need an uncoded web design for a new online dating web site called zMatchy.net. Simplicity and boldness are the key factors in the successful design.
Please look at the requirements document attached for details.
Updates
Dear all,
Please AVOID USING A PICTURE OF A HAPPY COUPLE ON THE HOME PAGE of the site. We highly want to move away from this space as it makes our web site just like another dating web site.
We like something simple with web 2.0 look and feel. The examples in the Requirements Document are exactly the design we are after.
Regards
Tarn
Industry/Entity Type
Dating
Look and feel
Each slider illustrates characteristics of the customer's brand and the style your logo design should communicate.

```html
<!DOCTYPE html>
<html lang="en">
<head>
<meta charset="utf-8">
<title>zMatchy.net – Browse</title>
<link rel="stylesheet" href="https://fonts.googleapis.com/css2?family=Arimo:wght@400;700&family=PT+Sans+Narrow:wght@700&family=Open+Sans:wght@600;700&display=swap">
<style>
:root{
  --bg:#2e2e2e;
  --bg-dark:#1f1f1f;
  --header:#050505;
  --footer:#232323;
  --red:#e3232b;
  --red-dark:#b5141a;
  --green:#7fe12a;
  --green-dark:#4fa812;
  --yellow:#e8cd2a;
  --yellow-dark:#c9a912;
  --white:#ffffff;
  --muted:#9a9a9a;
  --link-blue:#3b5998;
  --widget-border:#3a3a3a;
}
*{box-sizing:border-box;margin:0;padding:0}
html,body{width:1200px;height:773px;overflow:hidden}
body{position:relative;background:radial-gradient(ellipse at 50% 40%,#3a3a3a 0%,var(--bg) 45%,var(--bg-dark) 100%);font-family:"Arimo",Arial,sans-serif;color:var(--white)}
.site-header{position:absolute;left:0;top:0;width:1200px;height:41px;background:var(--header);box-shadow:0 2px 6px rgba(0,0,0,.6)}
.brand{position:absolute;display:flex;align-items:center;gap:4px;font-family:"Open Sans",sans-serif;font-weight:700}
.brand-dot{width:12px;height:12px;border-radius:50%;background:var(--red)}
.header-brand{left:187px;top:9px;font-size:20px;color:var(--red)}
.greeting{position:absolute;left:327px;top:14px;font-size:12.5px}
.main-nav{position:absolute;top:9px;left:0;width:1200px;height:24px}
.main-nav a{position:absolute;top:5px;font-size:12.5px;color:var(--white);text-decoration:none}
.main-nav .nav-mystuff{top:0;left:674px;width:70px;height:24px;line-height:24px;background:var(--yellow);color:#333;border-radius:3px;text-align:center}
.nav-mystuff::after{content:"";display:inline-block;margin-left:3px;border:4px solid transparent;border-top-color:#333;vertical-align:-1px}
.tag-list{position:absolute;left:186px;top:129px;list-style:none}
.tag{width:87px;height:24px;margin-bottom:8.4px;background:#050505;border-radius:12px;font-size:11px;line-height:24px;padding-left:11px}
.video-player{position:absolute;left:309px;top:80px;width:561px;height:315px;background:#000}
.play-button{position:absolute;left:553px;top:192px}
.message-box{position:absolute;left:480px;top:408px;width:219px;height:92px;background:var(--white);border:none;border-radius:4px;padding:8px 9px;font-family:"Arimo",sans-serif;font-size:11px;color:#999;resize:none}
.action{position:absolute;top:518px;width:102px;height:37px;border-radius:2px;font-family:"PT Sans Narrow",sans-serif;font-size:18px;text-align:center;line-height:36px;color:#111}
.action-friends{left:343px;background:linear-gradient(var(--green),var(--green-dark))}
.action-woo{left:537px;background:linear-gradient(#f02a2f,var(--red-dark))}
.action-next{left:735px;background:linear-gradient(#f2d93a,var(--yellow-dark))}
.social-widget{position:absolute;left:905px;top:81px;width:155px;height:448px;background:var(--white);border:1px solid var(--widget-border);color:#333;font-size:9px}
.widget-head{height:71px;border-bottom:1px solid #ddd;text-align:center}
.widget-brand{position:relative;justify-content:center;width:100%;top:6px;font-size:17px;color:var(--red)}
.widget-like{position:absolute;left:16px;top:41px;display:flex;gap:12px;align-items:center;font-size:10px}
.like-btn{border:1px solid #c4cde0;background:#eceef5;padding:3px 5px;border-radius:2px;color:var(--link-blue)}
.widget-like span:last-child{color:var(--link-blue)}
.widget-feed{position:relative;height:264px;overflow:hidden;border-bottom:1px solid #ddd;padding:10px 18px 0 8px}
.feed-author{display:flex;align-items:center;gap:8px;font-size:11px;color:var(--link-blue);margin-bottom:6px}
.feed-author .brand-dot{width:20px;height:20px}
.feed-post{line-height:12.3px;color:#111;width:100px}
.feed-time{color:#999;margin:6px 0 14px}
.scrollbar{position:absolute;right:3px;top:2px;width:11px;height:258px;background:#f0f0f0;border-left:1px solid #ddd}
.scrollbar::before{content:"";position:absolute;left:1px;top:16px;width:8px;height:32px;background:#d8d8d8;border:1px solid #bbb}
.widget-fans{padding:6px 8px}
.widget-fans b{font-weight:400;color:var(--link-blue);font-size:11px}
.fan-row{display:flex;gap:8px;margin-top:6px;text-align:center;color:#777;font-size:8.5px}
.fan-photo{width:44px;height:44px;margin-bottom:4px}
.widget-foot{position:absolute;bottom:0;left:0;width:100%;height:22px;border-top:1px solid #ddd;display:flex;align-items:center;gap:5px;padding-left:8px;font-size:8.5px;color:#555}
.widget-foot i{width:12px;height:12px;background:var(--link-blue)}
.contact-tab{position:absolute;left:547px;top:586px;width:106px;height:35px;background:#0d0d0d;border-radius:5px 5px 0 0;font-family:"PT Sans Narrow",sans-serif;font-size:16px;display:flex;align-items:center;justify-content:center;gap:6px}
.site-footer{position:absolute;left:0;top:621px;width:1200px;height:152px;background:var(--footer);box-shadow:inset 0 6px 10px rgba(0,0,0,.5)}
.footer-title{position:absolute;font-family:"PT Sans Narrow",sans-serif;font-size:20px;color:#ee3a3a}
.read-more{left:187px;top:16px}
.share-title{left:515px;top:16px}
.footer-links{position:absolute;left:186px;top:44px;list-style:none}
.footer-links li{font-family:"PT Sans Narrow",sans-serif;font-size:13.5px;height:21.2px;display:flex;align-items:center;gap:4px}
.footer-links li::before{content:"→";color:#ee3a3a;font-family:"Arimo",sans-serif;font-size:13px}
.share-grid{position:absolute;left:514px;top:45px;display:grid;grid-template-columns:repeat(4,23px);gap:4px 8px}
.share-grid span{width:23px;height:23px;border-radius:3px;background:#5c5c5c}
.footer-legal{position:absolute;left:814px;top:29px;width:200px;text-align:center;font-family:"Open Sans",sans-serif;font-weight:700;font-size:11px}
.footer-brand{position:relative;justify-content:center;width:100%;margin:16px 0 12px;font-size:30px;color:#ececec}
.footer-brand .brand-dot{width:18px;height:18px;background:#ececec}
</style>
</head>
<body>
<header class="site-header">
  <div class="brand header-brand"><span class="brand-dot"></span>zMatchy</div>
  <div class="greeting">Greetings, Tarn</div>
  <nav class="main-nav">
    <a class="nav-mystuff" href="#">My Stuff</a>
    <a href="#" style="left:766px">My Messages</a>
    <a href="#" style="left:868px">Start Dating</a>
    <a href="#" style="left:961px">Sign Out</a>
    <a href="#" style="left:1040px">Help</a>
  </nav>
</header>

<ul class="tag-list">
  <li class="tag">Tag1</li><li class="tag">Tag1</li><li class="tag">Tag1</li><li class="tag">Tag1</li><li class="tag">Tag1</li><li class="tag">Tag1</li><li class="tag">Tag1</li>
</ul>

<div class="video-player" role="img" aria-label="Member video profile player"></div>
<svg class="play-button" width="74" height="74" viewBox="0 0 74 74" aria-hidden="true">
  <defs><linearGradient id="playFill" x1="0" y1="0" x2="0" y2="1"><stop offset="0" stop-color="#555"/><stop offset="1" stop-color="#1a1a1a"/></linearGradient></defs>
  <circle cx="37" cy="37" r="34" fill="url(#playFill)" stroke="#bdbdbd" stroke-width="4"/>
  <path d="M29 22 L53 37 L29 52 Z" fill="#e5e5e5"/>
</svg>

<textarea class="message-box" placeholder="Type Your Message Here..."></textarea>

<div class="action action-friends">Be Friends</div>
<div class="action action-woo">Woo Me</div>
<div class="action action-next">Next</div>

<aside class="social-widget">
  <div class="widget-head">
    <div class="brand widget-brand"><span class="brand-dot"></span>zMatchy</div>
    <div class="widget-like"><span class="like-btn">Like</span><span>on FriendWall</span></div>
  </div>
  <div class="widget-feed">
    <div class="feed-author"><span class="brand-dot"></span>zmatchy</div>
    <p class="feed-post">Dr. Lena brought us all some awesome bagels today to celebrate a hard work week! Repaired a lot of broken teeth this week. Maybe a lot of early Halloween candy? Remember to avoid the sticky ones! Happy Thursday:))</p>
    <p class="feed-time">Yesterday at 2:47am</p>
    <p class="feed-post">Dr. Lena brought us all some awesome bagels today to celebrate a hard work week! Repaired a lot</p>
    <div class="scrollbar"></div>
  </div>
  <div class="widget-fans">
    290 people like <b>zmatchy</b>
    <div class="fan-row">
      <div><div class="fan-photo" role="img" aria-label="Fan page picture" style="background:linear-gradient(135deg,#7a3c6a,#c4a04a)"></div>Qtrv</div>
      <div><div class="fan-photo" role="img" aria-label="Default member picture" style="background:#c9cfe0"></div>Rosalind</div>
    </div>
  </div>
  <div class="widget-foot"><i></i>FriendWall social plugin</div>
</aside>

<div class="contact-tab">Contact Us
  <svg width="18" height="18" viewBox="0 0 18 18" aria-hidden="true"><path d="M9 1 L16 9 H11 V17 H7 V9 H2 Z" fill="#fff"/></svg>
</div>

<footer class="site-footer">
  <h2 class="footer-title read-more">Read More</h2>
  <ul class="footer-links">
    <li>Why zMatchy</li><li>How it works</li><li>Sign Up</li><li>Login</li><li>About Us</li>
  </ul>
  <h2 class="footer-title share-title">Share This</h2>
  <div class="share-grid" aria-label="Share links">
    <span></span><span></span><span></span><span></span><span></span><span></span><span></span><span></span>
  </div>
  <div class="footer-legal">
    <p>© 2011 zMatchy &nbsp;|&nbsp; All Rights Reserved</p>
    <div class="brand footer-brand"><span class="brand-dot"></span>zMatchy</div>
    <p>Privacy Policy &nbsp;|&nbsp; Terms &amp; Conditions</p>
  </div>
</footer>
</body>
</html>
```